3 pages of UI design for AdTech Startup

We need 3 pages of UI design for a new AdTech company located in Seattle called KELVRA Systems.

We put digital, mobile billboards on college campuses throughout the country. This design project involves our back-end customer dashboard.

Page 1- Dashboard home page
page 2- Manage ads screen (see File 3 below for the screenshot of our current design). Please match the design of all 3 screens so there is consistency
page 3-Detailed Zone screen (see file 16 below). This page looks similar to the first page but gives a more detailed overview and a larger map.

The features and functionality are already built but we are lacking an aesthetically pleasing and slick design. Looking for someone who can match our website look to this new dashboard space. Our company reflects modern, clean, elegant design that is straight-forward and user friendly (main inspiration is TROVI, we love their design and feel).

Target Market(s)

-Local business owner, marketing directors, and national advertising and marketing agencies

Industry/Entity Type

Advertising

Number of Pages Required

3 page

Font styles to use
Other font styles liked:
• Proxima Nova- Thin for body text, Light for title

Colors
85cae6
33a6d7
0292cd
ffffff

Requirements
Nice to have
• Please include enough detail so that my developer can look at the design you come up with and translate it to html. Please include spacing, fonts, color numbers. My developer is going to look at your creation and recreate it in html format

```html
<!DOCTYPE html>
<html lang="en">
<head>
<meta charset="utf-8">
<title>KELVRA Systems – Dashboard</title>
<link rel="stylesheet" href="https://fonts.googleapis.com/css2?family=Lato:wght@300;400;700&display=swap">
<style>
  :root{
    --sky:#85cae6;
    --blue:#33a6d7;
    --blue-deep:#0292cd;
    --white:#ffffff;
    --page:#eef1f8;
    --ink:#333333;
    --muted:#8a8a8a;
    --line:#e3e3e3;
    --panel-head:#f5f5f5;
    --alert:#e05a6a;
    --teal:#4fc6bf;
    --amber:#f4c84a;
    --coral:#ef6a5e;
    --steel:#4a86d0;
    --footer:#333333;
    --photo:#a0602e;
    --map:#6f7a58;
  }
  *{box-sizing:border-box;margin:0;padding:0}
  html,body{width:1200px;height:874px;overflow:hidden}
  body{position:relative;background:var(--page);font-family:"Lato",sans-serif;color:var(--ink)}
  .abs{position:absolute}

  /* header */
  .topbar{left:0;top:0;width:1200px;height:83px;background:var(--white);box-shadow:0 1px 4px rgba(0,0,0,.12)}
  .brand{left:99px;top:18px;font-size:42px;font-weight:300;letter-spacing:1px;color:var(--blue)}
  .partner{left:675px;top:28px;font-size:22px;font-weight:700;color:#1d4f9c}
  .avatar{left:758px;top:21px;width:41px;height:41px;border-radius:50%;background:#9aa0a6}
  .avatar-dot{left:791px;top:21px;width:9px;height:9px;border-radius:50%;background:#7ccd3c;border:1px solid var(--white)}
  .user{left:813px;top:33px;font-size:14px;font-weight:700}
  .sep{top:28px;width:1px;height:27px;background:#d0d0d0}
  .nav-link{top:33px;font-size:14px;font-weight:700;display:flex;align-items:center;gap:7px}

  /* breadcrumb */
  .crumbs{left:99px;top:123px;width:1002px;height:32px;background:var(--white)}
  .crumb-home{left:99px;top:123px;width:150px;height:32px;background:var(--blue);color:var(--white);font-size:13px;font-weight:700;line-height:32px;padding-left:19px}
  .crumb-page{left:257px;top:123px;height:32px;line-height:32px;font-size:13px;color:#555;display:flex;align-items:center;gap:9px}
  .range-alert{left:883px;top:123px;width:218px;height:32px;background:var(--alert);color:var(--white);font-size:11px;font-weight:700;display:flex;align-items:center;gap:7px;padding-left:13px}

  /* statistics panel */
  .stats{left:99px;top:192px;width:751px;height:350px;background:var(--blue)}
  .stats-title{left:112px;top:201px;font-size:17px;font-weight:700;color:var(--white)}
  .stats-rule{left:99px;top:231px;width:751px;height:1px;background:rgba(255,255,255,.6)}
  .stats-divider{top:192px;width:1px;height:39px;background:rgba(255,255,255,.6)}
  .tabs{left:413px;top:196px;display:flex;gap:3px}
  .tab{height:31px;padding:0 11px;background:#f2f2f2;border:1px solid #cfcfcf;font-size:11px;font-weight:700;line-height:29px;color:#333}
  .tab.is-active{background:var(--blue-deep);color:var(--white);border-color:var(--blue-deep)}
  .stats-range{left:649px;top:201px;color:var(--white);font-size:11px;font-weight:700;display:flex;align-items:center;gap:7px}
  .chart{left:99px;top:232px}

  /* help panel */
  .help{left:882px;top:191px;width:219px;height:351px;background:var(--white);border:1px solid var(--line)}
  .panel-head{background:var(--panel-head);border-bottom:1px solid var(--line)}
  .help-head{left:882px;top:191px;width:219px;height:41px;padding-left:19px;line-height:41px;font-size:17px;font-weight:700;color:#444}
  .ring-label{font-size:14px;font-weight:300;color:var(--muted);text-align:center;width:100px}
  .ring-value{font-size:19px;font-weight:300;color:#777;text-align:center;width:80px}

  /* zone table */
  .zones{left:99px;top:582px;width:618px;height:213px;background:var(--white);border:1px solid var(--line)}
  .zones-head{left:99px;top:582px;width:618px;height:39px}
  .col-title{top:582px;height:39px;line-height:39px;text-align:center;font-size:17px;font-weight:700;color:#444}
  .col-line{top:582px;width:1px;height:196px;background:var(--line)}
  .zone-name{left:99px;top:658px;width:123px;text-align:center;font-size:17px;font-weight:700;color:var(--blue-deep)}
  .zone-sub{left:99px;top:679px;width:123px;text-align:center;font-size:12px}
  .venue-photo{left:229px;top:637px;width:99px;height:79px;border-radius:3px;background:linear-gradient(180deg,#3b2b24 0%,var(--photo) 45%,#c9a162 70%,#5a2f22 100%)}
  .btn-manage{left:229px;top:731px;width:99px;height:27px;background:var(--blue-deep);color:var(--white);font-size:15px;font-weight:700;line-height:27px;text-align:center}
  .route-map{left:345px;top:637px;width:358px;height:127px;border-radius:5px;background:linear-gradient(135deg,#5f6a4a 0%,var(--map) 50%,#8a8d7a 100%)}

  /* zone performance */
  .perf{left:729px;top:582px;width:372px;height:213px;background:var(--white);border:1px solid var(--line)}
  .perf-head{left:729px;top:582px;width:372px;height:39px;line-height:39px;text-align:center;font-size:17px;font-weight:700;color:#444}
  .btn{top:751px;height:27px;line-height:27px;font-size:12px;text-align:center;color:var(--white)}
  .btn-text{left:831px;width:102px;background:var(--blue-deep)}
  .btn-details{left:935px;width:63px;background:#333;font-weight:700}

  /* footer */
  .footer{left:0;top:832px;width:1200px;height:42px;background:var(--footer);color:var(--white);font-size:14px;text-align:center;line-height:42px}
</style>
</head>
<body>

<header class="abs topbar"></header>
<div class="abs brand">KELVRA</div>
<div class="abs partner">VANTO</div>
<div class="abs avatar" role="img" aria-label="User profile photo"></div>
<div class="abs avatar-dot"></div>
<div class="abs user">Marcus Hale</div>
<div class="abs sep" style="left:905px"></div>
<div class="abs nav-link" style="left:923px">
  <svg width="18" height="18" viewBox="0 0 18 18"><circle cx="9" cy="9" r="9" fill="#33a6d7"/><text x="9" y="14" text-anchor="middle" font-family="Lato,sans-serif" font-size="13" font-weight="700" fill="#fff">?</text></svg>Help
</div>
<div class="abs sep" style="left:1004px"></div>
<div class="abs nav-link" style="left:1027px">
  <svg width="20" height="18" viewBox="0 0 20 18"><rect x="1" y="1" width="10" height="16" fill="#33a6d7"/><path d="M9 9h10M15 5l4 4-4 4" stroke="#33a6d7" stroke-width="2" fill="none"/></svg>Logout
</div>

<div class="abs crumbs"></div>
<div class="abs crumb-home">Insights Summary</div>
<div class="abs crumb-page">
  <svg width="7" height="11" viewBox="0 0 7 11"><path d="M1 1l5 4.5L1 10" stroke="#555" fill="none"/></svg>Dashboard
</div>
<div class="abs range-alert">
  <svg width="18" height="18" viewBox="0 0 18 18"><rect x="1" y="3" width="16" height="14" fill="none" stroke="#fff" stroke-width="1.5"/><path d="M1 7h16M5 1v4M13 1v4M5 10h2M9 10h2M13 10h1M5 13h2M9 13h2" stroke="#fff" stroke-width="1.5"/></svg>
  29 July 2016 - 05 Aug 2016
  <svg width="14" height="8" viewBox="0 0 14 8" style="margin-left:6px"><path d="M1 1l6 6 6-6" stroke="#fff" fill="none"/></svg>
</div>

<section class="abs stats"></section>
<div class="abs stats-title">Statistics Graph</div>
<div class="abs stats-rule"></div>
<div class="abs stats-divider" style="left:406px"></div>
<div class="abs stats-divider" style="left:638px"></div>
<div class="abs tabs">
  <div class="tab">Hourly</div><div class="tab is-active">Day</div><div class="tab">Week</div><div class="tab">Month</div>
</div>
<div class="abs stats-range">
  <svg width="18" height="18" viewBox="0 0 18 18"><rect x="1" y="3" width="16" height="14" fill="none" stroke="#fff" stroke-width="1.5"/><path d="M1 7h16M5 1v4M13 1v4M5 10h2M9 10h2M13 10h1M5 13h2M9 13h2" stroke="#fff" stroke-width="1.5"/></svg>
  29 July 2016 - 05 Aug 2016
  <svg width="14" height="8" viewBox="0 0 14 8" style="margin-left:5px"><path d="M1 1l6 6 6-6" stroke="#fff" fill="none"/></svg>
</div>

<svg class="abs chart" width="751" height="310" viewBox="0 0 751 310" font-family="Lato,sans-serif">
  <g fill="#fff" font-size="12" text-anchor="end">
    <text x="31" y="40">100</text><text x="31" y="90">75</text><text x="31" y="141">50</text><text x="31" y="191">25</text><text x="31" y="242">0</text>
  </g>
  <line x1="45" y1="34" x2="45" y2="238" stroke="#fff"/>
  <line x1="45" y1="238" x2="714" y2="238" stroke="#fff"/>
  <g fill="#85cae6" opacity=".85">
    <rect x="71" y="189" width="30" height="49"/>
    <rect x="155" y="149" width="30" height="89"/>
    <rect x="239" y="157" width="30" height="81"/>
    <rect x="326" y="115" width="30" height="123"/>
    <rect x="416" y="143" width="30" height="95"/>
    <rect x="505" y="95" width="30" height="143"/>
    <rect x="594" y="103" width="30" height="135"/>
    <rect x="684" y="80" width="30" height="158"/>
  </g>
  <g stroke="#fff">
    <line x1="86" y1="238" x2="86" y2="244"/><line x1="170" y1="238" x2="170" y2="244"/><line x1="254" y1="238" x2="254" y2="244"/><line x1="341" y1="238" x2="341" y2="244"/><line x1="431" y1="238" x2="431" y2="244"/><line x1="520" y1="238" x2="520" y2="244"/><line x1="609" y1="238" x2="609" y2="244"/><line x1="699" y1="238" x2="699" y2="244"/>
  </g>
  <polyline points="68,225 151,192 236,192 323,167 412,183 501,141 591,149 680,123" fill="none" stroke="#0292cd" stroke-width="1"/>
  <g fill="#fff" stroke="#0292cd" stroke-width="1.5">
    <circle cx="68" cy="225" r="3"/><circle cx="151" cy="192" r="3"/><circle cx="236" cy="192" r="3"/><circle cx="323" cy="167" r="3"/><circle cx="412" cy="183" r="3"/><circle cx="501" cy="141" r="3"/><circle cx="591" cy="149" r="3"/><circle cx="680" cy="123" r="3"/>
  </g>
  <g fill="#fff" font-size="11" font-weight="700" text-anchor="middle">
    <text x="86" y="278">Jul 29,2016</text><text x="170" y="278">Jul 30,2016</text><text x="254" y="278">Jul 31,2016</text><text x="341" y="278">Aug 01,2016</text><text x="431" y="278">Aug 02,2016</text><text x="520" y="278">Aug 03,2016</text><text x="609" y="278">Aug 04,2016</text><text x="699" y="278">Aug 05,2016</text>
  </g>
</svg>

<aside class="abs help"></aside>
<div class="abs panel-head help-head">Help</div>
<svg class="abs" style="left:882px;top:232px" width="219" height="310" viewBox="0 0 219 310">
  <circle cx="62" cy="77" r="38" fill="none" stroke="#4fc6bf" stroke-width="1.5" stroke-dasharray="220 19" transform="rotate(-60 62 77)"/>
  <circle cx="163" cy="77" r="38" fill="none" stroke="#f4c84a" stroke-width="1.5"/>
  <circle cx="62" cy="208" r="38" fill="none" stroke="#ef6a5e" stroke-width="1.5"/>
  <circle cx="163" cy="208" r="38" fill="none" stroke="#4a86d0" stroke-width="1.5"/>
</svg>
<div class="abs ring-value" style="left:904px;top:301px">85%</div>
<div class="abs ring-value" style="left:1005px;top:297px">21:25</div>
<div class="abs ring-value" style="left:1005px;top:321px;font-size:13px">min</div>
<div class="abs ring-value" style="left:904px;top:431px">595</div>
<div class="abs ring-value" style="left:1005px;top:431px">0.3</div>
<div class="abs ring-label" style="left:894px;top:353px">Rotations</div>
<div class="abs ring-label" style="left:894px;top:486px">Impressions</div>
<div class="abs ring-label" style="left:998px;top:488px">Miles</div>

<section class="abs zones"></section>
<div class="abs panel-head zones-head"></div>
<div class="abs col-line" style="left:222px"></div>
<div class="abs col-line" style="left:333px"></div>
<div class="abs col-title" style="left:99px;width:123px">Zone</div>
<div class="abs col-title" style="left:222px;width:111px">Active</div>
<div class="abs col-title" style="left:333px;width:384px">Carrier parth</div>
<div class="abs zone-name">Zone 1</div>
<div class="abs zone-sub">Rowan's House</div>
<div class="abs venue-photo" role="img" aria-label="Photo of an indoor basketball arena"></div>
<div class="abs btn-manage">Manage</div>
<div class="abs route-map" role="img" aria-label="Satellite map of the carrier route near Rowan's House"></div>

<section class="abs perf"></section>
<div class="abs panel-head perf-head">Zone Performance</div>
<svg class="abs" style="left:729px;top:621px" width="372" height="120" viewBox="0 0 372 120">
  <circle cx="58" cy="53" r="35" fill="none" stroke="#4fc6bf" stroke-width="1.5" stroke-dasharray="200 20" transform="rotate(-60 58 53)"/>
  <circle cx="174" cy="53" r="35" fill="none" stroke="#f4c84a" stroke-width="1.5"/>
  <circle cx="307" cy="53" r="35" fill="none" stroke="#4a86d0" stroke-width="1.5"/>
</svg>
<div class="abs ring-value" style="left:747px;top:667px;font-size:18px">85%</div>
<div class="abs ring-value" style="left:863px;top:664px;font-size:18px">21:25</div>
<div class="abs ring-value" style="left:863px;top:686px;font-size:12px">min</div>
<div class="abs ring-value" style="left:996px;top:665px;font-size:18px">0.3</div>
<div class="abs ring-label" style="left:737px;top:715px;font-size:13px">Rotations</div>
<div class="abs ring-label" style="left:843px;top:715px;font-size:13px;width:120px">Broadcast time</div>
<div class="abs ring-label" style="left:978px;top:715px;font-size:13px;width:120px">Miles Walked</div>
<div class="abs btn btn-text">Text Messages</div>
<div class="abs btn btn-details">Details</div>

<footer class="abs footer">Copyright © 2016 Kelvra. All Rights Reserved.</footer>

</body>
</html>
```